Website for a Construction Business That Builds Houses

We want some design concepts for this website. Customer likes this competitor site: https://brenwickdwellings.com.au/

We have a logo for Tarvond Constructions. Logo font is Birdman, attached with AI.

Want to be able to change hero images

Will have a contact page.

Need to know what plugins will be used for WordPress.

Coding

Coded - Design and coding required

```html
<!DOCTYPE html>
<html lang="en">
<head>
<meta charset="utf-8">
<title>Tarvond Constructions – Building Your Dream Home</title>
<link rel="stylesheet" href="https://fonts.googleapis.com/css2?family=Audiowide&family=Kaushan+Script&family=Montserrat:wght@400;500;600;700&display=swap">
<style>
:root{
  --green:#8dc63f;
  --green-dark:#7ab32f;
  --ink:#1c1c1c;
  --body:#3a3a3a;
  --grey-bg:#efefef;
  --field:#ebebeb;
  --footer:#1b2114;
  --star:#f7931e;
  --white:#fff;
}
*{box-sizing:border-box;margin:0;padding:0}
html,body{width:1200px;height:4601px;overflow:hidden}
body{font-family:"Montserrat",sans-serif;color:var(--ink);background:var(--white);position:relative}
section,header,footer{position:relative;width:1200px}
.abs{position:absolute}
.display{font-family:"Audiowide",sans-serif;text-transform:uppercase;font-weight:400;letter-spacing:1px}
.display .hl{color:var(--green)}
.eyebrow{font-family:"Kaushan Script",cursive;font-size:20px;display:flex;align-items:center;gap:10px;color:var(--ink)}
.eyebrow::before{content:"";width:36px;height:3px;background:var(--green);border-radius:2px}
.btn{position:absolute;display:flex;align-items:center;justify-content:center;background:var(--green);color:var(--white);font-size:12px;font-weight:500;border-radius:3px;text-decoration:none}
.photo{position:absolute}
p{font-size:12.5px;line-height:23px;color:var(--body)}

/* header */
.site-header{height:84px;background:var(--white)}
.brand{position:absolute;left:141px;top:16px;color:var(--green);font-weight:700;line-height:1}
.brand .name{font-size:24px;display:block}
.brand .sub{font-size:9px;display:block;letter-spacing:1px;margin-top:4px}
.nav-home{left:855px;top:33px;font-size:12px;font-weight:600}
.nav-home::after{content:"";position:absolute;left:0;right:0;bottom:-7px;height:2px;background:var(--green)}

/* hero */
.hero{height:530px}
.hero-photo{inset:0;background:linear-gradient(180deg,#7fa0d8 0%,#a9c0e8 45%,#dfe6f1 68%,#6f9a3b 78%,#3f7023 100%)}
.hero-house{left:480px;top:90px;width:660px;height:345px;background:linear-gradient(180deg,#c9c9d1,#eeeef2);border-radius:4px}
.hero-title{left:140px;top:105px;font-size:46px;line-height:50px;color:var(--ink);text-transform:none;letter-spacing:2px}
.hero-text{left:140px;top:270px;width:340px;font-size:13px;line-height:20px;color:var(--ink)}
.hero .btn{left:141px;top:325px;width:141px;height:42px}

/* about */
.about{height:550px}
.about .eyebrow{position:absolute;left:141px;top:108px}
.about h2{left:141px;top:140px;font-size:28px;line-height:36px}
.about-img-small{left:141px;top:248px;width:233px;height:247px;background:linear-gradient(180deg,#c4cbd4,#5a5f66 60%,#6b7d4d)}
.about-img-large{left:705px;top:116px;width:354px;height:380px;background:linear-gradient(180deg,#dfe3ea,#b7b9b6 60%,#8b8f84)}
.about-copy{left:405px;top:246px;width:270px}
.about-copy p+p{margin-top:8px}
.about .btn{left:405px;top:454px;width:127px;height:41px}

/* services */
.services{height:681px;background:linear-gradient(180deg,#fff 0%,#f6f6f6 45%,#efefef 100%)}
.services .eyebrow{position:absolute;left:0;right:0;top:86px;justify-content:center}
.services h2{left:0;right:0;top:122px;text-align:center;font-size:30px}
.card-photo{top:179px;width:289px;height:302px}
.svc-label{top:500px;display:flex;align-items:center;gap:16px;font-size:14px;font-weight:700;text-transform:uppercase}
.svc-label b{font-family:"Audiowide",sans-serif;color:var(--green);font-size:30px;font-weight:400}
.services .btn{left:536px;top:552px;width:127px;height:41px}

/* portfolio */
.portfolio{height:745px;background:var(--grey-bg)}
.portfolio .eyebrow{position:absolute;left:141px;top:92px}
.portfolio h2{left:139px;top:128px;font-size:28px}
.portfolio .btn{left:930px;top:98px;width:127px;height:39px}
.tile{width:293px;height:236px}
.tile-overlay{left:605px;top:423px;width:292px;height:236px;background:rgba(40,44,48,.82);border-right:4px solid var(--green);color:var(--white);text-align:center;padding-top:52px}
.tile-overlay h3{font-size:15px;font-weight:600;margin-bottom:10px}
.tile-overlay p{color:#ddd;font-size:12px;line-height:19px;width:260px;margin:0 auto}
.tile-overlay span{display:inline-block;margin-top:12px;color:var(--green);font-size:12px;text-decoration:underline}

/* testimonials */
.testimonials{height:637px}
.testimonials .eyebrow{position:absolute;left:0;right:0;top:98px;justify-content:center}
.testimonials h2{left:0;right:0;top:134px;text-align:center;font-size:28px}
.review{top:178px;width:289px;height:372px;border:1px solid #e3e3e3;text-align:center;padding-top:30px}
.avatar{width:64px;height:64px;border-radius:50%;border:3px solid var(--green);background:#c8d1c0;margin:0 auto 22px}
.review p{font-size:12px;line-height:23px;width:250px;margin:0 auto}
.review h4{font-size:15px;font-weight:700;margin-top:18px}
.stars{display:flex;justify-content:center;gap:5px;margin-top:6px}
.arrow{top:348px;width:34px;height:34px;border-radius:50%;display:flex;align-items:center;justify-content:center}
.arrow.prev{left:69px;background:var(--white);box-shadow:0 1px 6px rgba(0,0,0,.15)}
.arrow.next{left:1094px;background:var(--green)}

/* benefits */
.benefits{height:441px;background:var(--green)}
.benefits-photo{left:0;top:0;width:600px;height:441px;background:linear-gradient(180deg,#8ea3b7,#c9c6c0 45%,#6f6558 100%)}
.benefits .eyebrow{position:absolute;left:650px;top:78px}
.benefits .eyebrow::before{background:var(--ink)}
.benefits h2{left:650px;top:112px;font-size:28px;color:var(--ink)}
.benefits-copy{left:650px;top:152px;width:408px}
.benefits-copy p{font-size:12.5px;color:#1f2a10}
.benefits-copy p+p{margin-top:10px}
.benefits .btn{left:650px;top:323px;width:127px;height:42px;background:var(--ink)}

/* contact */
.inquiry{height:566px}
.inquiry .eyebrow{position:absolute;left:0;right:0;top:90px;justify-content:center}
.inquiry h2{left:0;right:0;top:126px;text-align:center;font-size:28px}
.field{position:absolute;background:var(--field);font-size:11px;color:#444;padding:0 18px;display:flex;align-items:center;height:46px;width:311px}
.field.active{background:var(--white);border:2px solid var(--green)}
.field.active span{border-right:1px solid #333;padding-right:14px}
.field-tag{position:absolute;left:280px;top:395px;background:var(--green);color:var(--white);font-size:9px;padding:2px 10px}
.field.msg{align-items:flex-start;padding-top:16px;height:92px;width:640px}
.submit{position:absolute;left:281px;top:370px;width:639px;height:46px;background:var(--green);color:var(--white);font-size:12px;display:flex;align-items:center;justify-content:center}

/* footer */
.site-footer{height:367px;background:var(--footer);color:var(--white)}
.foot-brand{left:141px;top:90px;color:var(--green);font-weight:700;line-height:1}
.foot-brand .name{font-size:56px;display:block}
.foot-brand .sub{font-size:22px;display:block;margin-top:8px;letter-spacing:2px}
.foot-col h5{font-family:"Audiowide",sans-serif;font-weight:400;font-size:14px;text-transform:uppercase;letter-spacing:1px;margin-bottom:20px}
.foot-col h5 .hl{color:var(--green)}
.foot-col li{list-style:none;font-size:12px;line-height:18px;margin-bottom:23px;display:flex;gap:10px}
.foot-col li svg{flex:none;margin-top:2px}
.foot-col strong{font-weight:500;display:block}
.foot-rule{left:141px;right:141px;top:333px;height:1px;background:#3b4230}
.copyright{left:0;right:0;top:342px;text-align:center;font-size:11px}
</style>
</head>
<body>

<header class="site-header">
  <div class="brand"><span class="name">tarvond</span><span class="sub">constructions</span></div>
  <span class="abs nav-home">Home</span>
  <a class="btn" style="left:932px;top:21px;width:127px;height:42px">Contact Us</a>
</header>

<section class="hero">
  <div class="photo hero-photo" role="img" aria-label="Large white two-storey house with trees and green lawn under a blue sky"></div>
  <div class="photo hero-house" role="img" aria-label="Detail of the white multi-level home facade"></div>
  <h1 class="abs display hero-title">Building your<br>dream home<br>in australia</h1>
  <p class="abs hero-text">Lorem Ipsum is simply dummy text of the printing &amp; typesetting industry.</p>
  <a class="btn">Get A Free Quote</a>
</section>

<section class="about">
  <div class="eyebrow">About Us</div>
  <h2 class="abs display">About Tarvond<br><span class="hl">Constructions</span></h2>
  <div class="photo about-img-small" role="img" aria-label="Modern grey two-storey house at dusk"></div>
  <div class="abs about-copy">
    <p>Lorem ipsum dolor sit amet, consectetur adipiscing elit, sed do eiusmod tempor ex ut incididunt ut labore et dolore magna aliqua. Ut enim ad minim veniam, quis nostrud amet exercitation ullamco laboris nisi ut aliquip ex ea commodo consequat.</p>
    <p>Ut enim ad minim veniam, quis nostrud amet exercitation ullamco laboris.</p>
  </div>
  <a class="btn">Read More</a>
  <div class="photo about-img-large" role="img" aria-label="Traditional grey house with white porch and front steps"></div>
</section>

<section class="services">
  <div class="eyebrow">Our Services</div>
  <h2 class="abs display">What we <span class="hl">do</span></h2>
  <div class="photo card-photo" style="left:141px;background:linear-gradient(180deg,#9fc1e4,#c9a98a 60%,#5d4a3c)" role="img" aria-label="Builder in hard hat reading construction plans"></div>
  <div class="photo card-photo" style="left:455px;background:linear-gradient(180deg,#e9e9e7,#cfcfcc 60%,#8d8f92)" role="img" aria-label="Two workers renovating an interior wall"></div>
  <div class="photo card-photo" style="left:770px;background:linear-gradient(180deg,#6f8a6a,#3b3f3a 55%,#c48d4a 75%,#2f3a3f)" role="img" aria-label="Modern home extension lit at dusk beside a pool"></div>
  <div class="abs svc-label" style="left:194px"><b>01</b>Home Building</div>
  <div class="abs svc-label" style="left:515px"><b>02</b>Renovations</div>
  <div class="abs svc-label" style="left:837px"><b>03</b>Extensions</div>
  <a class="btn">Read More</a>
</section>

<section class="portfolio">
  <div class="eyebrow">Our Portfolio</div>
  <h2 class="abs display">Project <span class="hl">Gallery</span></h2>
  <a class="btn">View More</a>
  <div class="photo tile" style="left:0;top:178px;background:linear-gradient(180deg,#b9cde2,#5c5a57 55%,#7a7b78)" role="img" aria-label="Modern house with double garage"></div>
  <div class="photo tile" style="left:302px;top:178px;background:linear-gradient(180deg,#f0c98a,#9a8a78 55%,#5d7a36)" role="img" aria-label="Family home at sunset"></div>
  <div class="photo tile" style="left:605px;top:178px;background:linear-gradient(180deg,#a8c6e6,#3c3f42 55%,#6e6e6c)" role="img" aria-label="Contemporary dark home with long driveway"></div>
  <div class="photo tile" style="left:907px;top:178px;background:linear-gradient(180deg,#9fbde0,#eef0f2 50%,#5c7e3a)" role="img" aria-label="White gabled house with timber door"></div>
  <div class="photo tile" style="left:0;top:423px;background:linear-gradient(180deg,#bed1e5,#6b5e52 55%,#585b5c)" role="img" aria-label="Two-storey modern home with timber cladding"></div>
  <div class="photo tile" style="left:302px;top:423px;background:linear-gradient(180deg,#c8d9ec,#e6e6e3 50%,#5e7a3e)" role="img" aria-label="White modern home with flat roof"></div>
  <div class="photo tile" style="left:605px;top:423px;background:linear-gradient(180deg,#55606a,#2f3338)" role="img" aria-label="Manor house at dusk"></div>
  <div class="abs tile-overlay">
    <h3>Majestic Manor</h3>
    <p>Ut enim ad minim veniam, quis nostrud amet exercitation ullamco laboris.</p>
    <span>Read More</span>
  </div>
  <div class="photo tile" style="left:907px;top:423px;background:linear-gradient(180deg,#b7cce2,#66574b 55%,#8a8a86)" role="img" aria-label="Modern home with wide garage and paved drive"></div>
</section>

<section class="testimonials">
  <div class="eyebrow">Testimonials</div>
  <h2 class="abs display">What people <span class="hl">are saying</span></h2>
  <div class="abs arrow prev"><svg width="12" height="12" viewBox="0 0 12 12"><path d="M8 1 3 6l5 5" fill="none" stroke="#222" stroke-width="2"/></svg></div>
  <div class="abs arrow next"><svg width="12" height="12" viewBox="0 0 12 12"><path d="m4 1 5 5-5 5" fill="none" stroke="#fff" stroke-width="2"/></svg></div>

  <div class="abs review" style="left:141px">
    <div class="avatar" role="img" aria-label="Customer portrait"></div>
    <p>Lorem ipsum dolor sit amet, consectetur sit adipiscing elit, sed do eiusmod tempor ex ut incididunt ut labore et dolore magna aliqua. Ut enim ad minim veniam, quis nostrud amet exercitation ullamco laboris nisi ut aliquip ex ea commodo consequat.</p>
    <h4>Mark Dellow</h4>
    <div class="stars">
      <svg width="16" height="16" viewBox="0 0 24 24"><path d="m12 2 3 7 7.5.6-5.7 5 1.8 7.4L12 18l-6.6 4 1.8-7.4-5.7-5L9 9z" fill="var(--star)"/></svg><svg width="16" height="16" viewBox="0 0 24 24"><path d="m12 2 3 7 7.5.6-5.7 5 1.8 7.4L12 18l-6.6 4 1.8-7.4-5.7-5L9 9z" fill="var(--star)"/></svg><svg width="16" height="16" viewBox="0 0 24 24"><path d="m12 2 3 7 7.5.6-5.7 5 1.8 7.4L12 18l-6.6 4 1.8-7.4-5.7-5L9 9z" fill="var(--star)"/></svg><svg width="16" height="16" viewBox="0 0 24 24"><path d="m12 2 3 7 7.5.6-5.7 5 1.8 7.4L12 18l-6.6 4 1.8-7.4-5.7-5L9 9z" fill="var(--star)"/></svg><svg width="16" height="16" viewBox="0 0 24 24"><path d="m12 2 3 7 7.5.6-5.7 5 1.8 7.4L12 18l-6.6 4 1.8-7.4-5.7-5L9 9z" fill="var(--star)"/></svg>
    </div>
  </div>
  <div class="abs review" style="left:455px">
    <div class="avatar" role="img" aria-label="Customer portrait"></div>
    <p>Lorem ipsum dolor sit amet, consectetur sit adipiscing elit, sed do eiusmod tempor ex ut incididunt ut labore et dolore magna aliqua. Ut enim ad minim veniam, quis nostrud amet exercitation ullamco laboris nisi ut aliquip ex ea commodo consequat.</p>
    <h4>Fiona Harcastle</h4>
    <div class="stars">
      <svg width="16" height="16" viewBox="0 0 24 24"><path d="m12 2 3 7 7.5.6-5.7 5 1.8 7.4L12 18l-6.6 4 1.8-7.4-5.7-5L9 9z" fill="var(--star)"/></svg><svg width="16" height="16" viewBox="0 0 24 24"><path d="m12 2 3 7 7.5.6-5.7 5 1.8 7.4L12 18l-6.6 4 1.8-7.4-5.7-5L9 9z" fill="var(--star)"/></svg><svg width="16" height="16" viewBox="0 0 24 24"><path d="m12 2 3 7 7.5.6-5.7 5 1.8 7.4L12 18l-6.6 4 1.8-7.4-5.7-5L9 9z" fill="var(--star)"/></svg><svg width="16" height="16" viewBox="0 0 24 24"><path d="m12 2 3 7 7.5.6-5.7 5 1.8 7.4L12 18l-6.6 4 1.8-7.4-5.7-5L9 9z" fill="var(--star)"/></svg><svg width="16" height="16" viewBox="0 0 24 24"><path d="m12 2 3 7 7.5.6-5.7 5 1.8 7.4L12 18l-6.6 4 1.8-7.4-5.7-5L9 9z" fill="var(--star)"/></svg>
    </div>
  </div>
  <div class="abs review" style="left:770px">
    <div class="avatar" role="img" aria-label="Customer portrait"></div>
    <p>Lorem ipsum dolor sit amet, consectetur sit adipiscing elit, sed do eiusmod tempor ex ut incididunt ut labore et dolore magna aliqua. Ut enim ad minim veniam, quis nostrud amet exercitation ullamco laboris nisi ut aliquip ex ea commodo consequat.</p>
    <h4>Owen Pritchard</h4>
    <div class="stars">
      <svg width="16" height="16" viewBox="0 0 24 24"><path d="m12 2 3 7 7.5.6-5.7 5 1.8 7.4L12 18l-6.6 4 1.8-7.4-5.7-5L9 9z" fill="var(--star)"/></svg><svg width="16" height="16" viewBox="0 0 24 24"><path d="m12 2 3 7 7.5.6-5.7 5 1.8 7.4L12 18l-6.6 4 1.8-7.4-5.7-5L9 9z" fill="var(--star)"/></svg><svg width="16" height="16" viewBox="0 0 24 24"><path d="m12 2 3 7 7.5.6-5.7 5 1.8 7.4L12 18l-6.6 4 1.8-7.4-5.7-5L9 9z" fill="var(--star)"/></svg><svg width="16" height="16" viewBox="0 0 24 24"><path d="m12 2 3 7 7.5.6-5.7 5 1.8 7.4L12 18l-6.6 4 1.8-7.4-5.7-5L9 9z" fill="var(--star)"/></svg><svg width="16" height="16" viewBox="0 0 24 24"><path d="m12 2 3 7 7.5.6-5.7 5 1.8 7.4L12 18l-6.6 4 1.8-7.4-5.7-5L9 9z" fill="var(--star)"/></svg>
    </div>
  </div>
</section>

<section class="benefits">
  <div class="photo benefits-photo" role="img" aria-label="Builders installing windows on a new timber-clad house"></div>
  <div class="eyebrow">Our Benefits</div>
  <h2 class="abs display">Why choose us</h2>
  <div class="abs benefits-copy">
    <p>Lorem ipsum dolor sit amet, consectetur sit adipiscing elit, sed do eiusmod tempor ex ut incididunt ut labore et dolore magna aliqua. Ut enim ad minim veniam, quis nostrud amet exercitation ullamco laboris nisi ut aliquip ex ea commodo consequat.</p>
    <p>Excepteur sint occaecat cupidatat non proident, sunt in culpa qui officia deserunt mollit anim id est laborum.</p>
  </div>
  <a class="btn">Read More</a>
</section>

<section class="inquiry">
  <div class="eyebrow">Contact Form</div>
  <h2 class="abs display">Quick <span class="hl">Inquiry</span></h2>
  <span class="field-tag" style="top:155px">First Name*</span>
  <div class="field active" style="left:281px;top:169px"><span>John</span></div>
  <div class="field" style="left:609px;top:169px">Latest Name*</div>
  <div class="field" style="left:281px;top:230px">Email*</div>
  <div class="field" style="left:609px;top:230px">Phone*</div>
  <div class="field msg" style="left:281px;top:289px">Message</div>
  <div class="submit">Submit Now</div>
</section>

<footer class="site-footer">
  <div class="abs foot-brand"><span class="name">tarvond</span><span class="sub">constructions</span></div>

  <div class="abs foot-col" style="left:441px;top:64px">
    <h5>Quick <span class="hl">Links</span></h5>
    <ul><li>Home</li><li>Contact Us</li></ul>
  </div>

  <div class="abs foot-col" style="left:659px;top:64px;width:230px">
    <h5>Contact <span class="hl">Details</span></h5>
    <ul>
      <li><svg width="12" height="14" viewBox="0 0 12 14"><path d="M6 0a5 5 0 0 0-5 5c0 4 5 9 5 9s5-5 5-9a5 5 0 0 0-5-5zm0 7a2 2 0 1 1 0-4 2 2 0 0 1 0 4z" fill="#fff"/></svg><span>123, Building Name, Street<br>City, State XY 123456</span></li>
      <li><svg width="12" height="12" viewBox="0 0 24 24"><path d="M6.6 10.8a15 15 0 0 0 6.6 6.6l2.2-2.2a1 1 0 0 1 1-.3 11 11 0 0 0 3.6.6 1 1 0 0 1 1 1V20a1 1 0 0 1-1 1A17 17 0 0 1 3 4a1 1 0 0 1 1-1h3.5a1 1 0 0 1 1 1 11 11 0 0 0 .6 3.6 1 1 0 0 1-.3 1z" fill="#fff"/></svg><span><strong>Phone</strong>(123) 456-7890</span></li>
      <li><svg width="12" height="10" viewBox="0 0 24 18"><path d="M0 0h24v18H0z" fill="#fff"/><path d="m1 1 11 9 11-9" fill="none" stroke="#1b2114" stroke-width="2"/></svg><span><strong>Email</strong>info@tarvond.com</span></li>
    </ul>
  </div>

  <div class="abs foot-col" style="left:950px;top:64px">
    <h5>Follow <span class="hl">Us</span></h5>
    <ul>
      <li><svg width="10" height="10"><circle cx="5" cy="5" r="5" fill="#fff"/></svg>Chirpline</li>
      <li><svg width="10" height="10"><circle cx="5" cy="5" r="5" fill="#fff"/></svg>Folkpage</li>
      <li><svg width="10" height="10"><circle cx="5" cy="5" r="5" fill="#fff"/></svg>Snapgrid</li>
      <li><svg width="10" height="10"><circle cx="5" cy="5" r="5" fill="#fff"/></svg>Workweave</li>
    </ul>
  </div>

  <div class="abs foot-rule"></div>
  <p class="abs copyright" style="color:#fff">©2024 Tarvond Constructions. All Rights Reserved.</p>
</footer>

</body>
</html>
```